Mental Health care Company in Washington DC

We are a new mental health care services provider in Washington DC. Please look at these sites.
https://marlowbrookpartners.com
https://www.quillstoneinc.com
https://velmarsh-kt.org/
https://www.trivanqx.com
https://www.thelanternofqz.com

```html
<!DOCTYPE html>
<html lang="en">
<head>
<meta charset="utf-8">
<title>Velora Health — Mental Wellness in Washington, DC</title>
<link href="https://fonts.googleapis.com/css2?family=Montserrat:wght@400;500;600;700;800&display=swap" rel="stylesheet">
<style>
:root{
  --orange:#f5821f;
  --orange-deep:#f26b21;
  --ink:#2b2b2b;
  --navy:#1f2a4d;
  --muted:#8a8a8a;
  --teal:#8fd3d6;
  --line:#e4e4e4;
  --paper:#ffffff;
  --canvas:#f4f4f4;
}
*{box-sizing:border-box;margin:0;padding:0}
html,body{width:1200px;height:3854px;overflow:hidden}
body{background:var(--canvas);font-family:"Montserrat",sans-serif;color:var(--ink);position:relative}
.page{position:absolute;left:96px;top:0;width:1010px;height:3854px;background:var(--paper);box-shadow:0 0 40px rgba(0,0,0,.12);overflow:hidden}
.abs{position:absolute}
.photo{position:absolute}
.btn{position:absolute;background:var(--orange);color:#fff;font-weight:600;font-size:12px;display:flex;align-items:center;justify-content:center}
.brand{font-weight:600;color:var(--navy);letter-spacing:-.5px;display:flex;align-items:center;gap:8px;white-space:nowrap}
/* header */
.site-header{position:absolute;left:0;top:0;width:1010px;height:81px;background:#fff}
.nav{position:absolute;top:0;left:484px;height:81px;display:flex;font-size:12px;font-weight:500}
.nav a{color:var(--ink);text-decoration:none;display:flex;align-items:center;justify-content:center;height:81px;white-space:nowrap}
.nav a.active{background:var(--teal)}
/* hero */
.hero{position:absolute;left:0;top:81px;width:1010px;height:407px}
.hero-title{position:absolute;left:106px;top:152px;color:var(--orange);font-weight:800;font-size:37px;line-height:46px;letter-spacing:-1px}
.hero-sub{position:absolute;left:108px;top:293px;color:#fff;font-size:13px;line-height:18px;width:470px}
.hero-cta{position:absolute;left:607px;top:292px;width:217px;height:43px;border-radius:22px;background:#fff;border:2px solid var(--teal);display:flex;align-items:center;justify-content:center;font-size:18px;font-weight:500;white-space:nowrap}
.contact-band{position:absolute;left:0;top:488px;width:1010px;height:70px;background:var(--orange);color:#fff;display:flex}
.contact-band .item{flex:1;display:flex;flex-direction:column;justify-content:center;padding-left:86px;border-right:1px solid rgba(255,255,255,.5)}
.contact-band .item:last-child{border:none}
.contact-band b{font-size:18px;font-weight:500}
.contact-band small{font-size:10px;font-weight:600}
/* headings */
.h2{font-weight:700;font-size:32px;letter-spacing:-1px;color:var(--ink)}
.copy{font-size:10px;line-height:13px;color:var(--muted)}
.center{text-align:center}
/* services */
.card{position:absolute;top:1240px;width:194px;height:240px;background:#fff;box-shadow:0 2px 10px rgba(0,0,0,.15);text-align:center}
.card .pic{height:120px;background:linear-gradient(135deg,#d9cfc6,#7a6a60)}
.card .badge{width:38px;height:38px;border-radius:50%;background:#fff;border:3px solid #ddd;margin:-20px auto 0;position:relative}
.card h4{font-size:12px;font-weight:700;margin-top:6px}
.card p{font-size:10px;line-height:12px;color:#444;margin:4px 14px 0}
.card .more{display:inline-block;margin-top:8px;background:var(--orange);color:#fff;font-size:9px;font-weight:600;padding:2px 18px}
/* why */
.value{position:absolute;width:170px}
.value h5{font-size:14px;font-weight:500;color:#555;display:flex;align-items:center;gap:8px}
.value h5 i{width:10px;height:10px;border-radius:50%;background:var(--orange);display:inline-block}
.value p{font-size:8px;line-height:10px;color:var(--muted);margin-left:26px;margin-top:4px}
/* team */
.arch{position:absolute;top:2258px;width:128px;height:232px;border-radius:64px 64px 0 0;border:2px solid var(--teal);overflow:hidden}
.arch div{width:100%;height:100%}
/* testimonials */
.review{position:absolute;background:#fff;box-shadow:0 2px 12px rgba(0,0,0,.15);padding:14px 24px}
.review .who{display:flex;gap:8px;align-items:center;font-size:10px;line-height:12px;color:#444}
.review .who i{width:32px;height:32px;border-radius:50%;background:#9a8a80;flex:none}
.review.sm .who{font-size:6px;line-height:7px}
.review.sm .who i{width:20px;height:20px}
.review p{font-size:10px;line-height:12px;color:var(--muted);text-align:center;margin-top:14px}
.review.sm p{font-size:6px;line-height:7px;text-align:left;margin-top:8px}
.stars{color:#f4c542;text-align:center;font-size:14px;letter-spacing:2px}
.review.sm .stars{font-size:9px;text-align:left}
/* form */
.form label{position:absolute;font-size:15px;color:#444}
.form .field{position:absolute;left:186px;width:233px;border:1px solid #999;background:#fff}
/* footer */
.footer-links{position:absolute;top:3590px;left:534px;display:flex;gap:38px;font-size:12px;font-weight:600;white-space:nowrap}
.social{position:absolute;top:3742px;left:81px;display:flex;gap:8px}
.social i{width:18px;height:18px;border-radius:50%;background:var(--orange);display:block}
.copyright{position:absolute;left:0;top:3790px;width:1010px;height:64px;background:var(--orange);color:#fff;font-size:10px;display:flex;align-items:center;justify-content:center}
</style>
</head>
<body>
<main class="page">

  <header class="site-header">
    <div class="brand abs" style="left:74px;top:22px;font-size:29px"><span>Velora Health</span></div>
    <nav class="nav">
      <a class="active" style="width:76px">Home</a>
      <a style="width:80px">About</a>
      <a style="width:84px">Services</a>
      <a style="width:88px">Therapists</a>
      <a style="width:86px">Resources</a>
      <a style="width:80px">Contact</a>
    </nav>
  </header>

  <section class="hero">
    <div class="photo" role="img" aria-label="Two smiling clients in a bright therapy room" style="inset:0;background:linear-gradient(90deg,#1b1b1b 0%,#3a3038 35%,#6d5a4f 65%,#3b2f2a 100%)"></div>
    <h1 class="hero-title">Your Mental<br>Wellness<br>Starts Here</h1>
    <p class="hero-sub">Compassionate, personalized mental health care for individuals, couples, and families. In-office and virtual therapy available.</p>
    <a class="hero-cta">Get a Appoinment</a>
  </section>

  <div class="contact-band">
    <div class="item"><b>0800 555 41 276</b><small>For a free consultation</small></div>
    <div class="item" style="align-items:center;padding:0"><b>chat whith us</b><small>for more details</small></div>
    <div class="item" style="align-items:center;padding:0"><b>24/7 support</b><small>for more details</small></div>
  </div>

  <!-- about -->
  <section>
    <div class="abs" style="left:56px;top:605px;width:380px;height:230px;border-radius:120px 0 120px 120px;box-shadow:0 10px 30px rgba(0,0,0,.08)"></div>
    <div class="photo" role="img" aria-label="Group of cheerful young people in an office" style="left:76px;top:622px;width:335px;height:185px;border-radius:110px 0 110px 110px;border:2px solid #2d8bc9;background:linear-gradient(135deg,#5c6570,#c9c4bd 60%,#8a6f5e)"></div>
    <div class="abs" style="left:438px;top:780px;width:56px;height:56px;border-radius:50%;border:3px solid #e6e6e6"></div>
    <h2 class="h2 center abs" style="left:544px;top:638px;width:340px;font-size:30px;line-height:36px">Therapy That Meets You Where You Are</h2>
    <p class="copy abs" style="left:626px;top:722px;width:290px">At Velora Health, we provide modern, science-backed Located in the heart of Washington, DC, our licensed helping you find balance, clarity, and strength</p>
    <div class="abs" style="left:592px;top:780px;width:380px;height:230px;border-radius:120px 120px 120px 0;box-shadow:0 10px 30px rgba(0,0,0,.08)"></div>
    <div class="photo" role="img" aria-label="Woman enjoying sunset light outdoors" style="left:594px;top:798px;width:335px;height:186px;border-radius:110px 110px 110px 0;border:2px solid var(--orange);background:linear-gradient(180deg,#c6c0b5,#e8a45a 60%,#3e3a2c)"></div>
    <h2 class="h2 abs" style="left:93px;top:866px;font-size:30px">About Us</h2>
    <p class="copy abs" style="left:93px;top:912px;width:280px">At Velora Health, we provide modern, science-backed Located in the heart of Washington, DC, our licensed helping you find balance, clarity, and strength thr</p>
  </section>

  <!-- services -->
  <section>
    <svg class="abs" style="left:0;top:1080px" width="140" height="120"><path d="M0 0 A72 118 0 0 1 72 118 L0 118Z" fill="var(--orange-deep)"/><path d="M40 118 A45 36 0 0 1 136 118Z" fill="#d9d9d9"/></svg>
    <svg class="abs" style="left:880px;top:1480px" width="130" height="115"><path d="M130 2 A76 112 0 0 0 54 114 L130 114Z" fill="var(--orange-deep)"/><path d="M0 114 A45 36 0 0 1 80 114Z" fill="#d9d9d9"/></svg>
    <h2 class="h2 center abs" style="left:0;top:1098px;width:1010px">Our Services</h2>
    <p class="center abs" style="left:0;top:1145px;width:1010px;color:var(--orange);font-size:13px;font-weight:500">Therapy That Meets You Where You Are</p>
    <p class="copy center abs" style="left:250px;top:1176px;width:510px">At Velora Health, we provide modern, science-backed mental health services with a human touch. Located in the heart of Washington, DC, our licensed therapists are dedicated to</p>
    <article class="card" style="left:63px"><div class="pic" role="img" aria-label="Therapist comforting a client"></div><div class="badge"></div><h4>Lorem ipsum dolor</h4><p>consectetur adipiscing elit, sed do eiusmod tempor</p><span class="more">View All</span></article>
    <article class="card" style="left:298px"><div class="pic" role="img" aria-label="Two people giving a high five" style="background:linear-gradient(135deg,#e8e2da,#8d7a6d)"></div><div class="badge"></div><h4>Lorem ipsum dolor</h4><p>consectetur adipiscing elit, sed do eiusmod tempor</p><span class="more">View All</span></article>
    <article class="card" style="left:520px"><div class="pic" role="img" aria-label="Two men sharing a supportive hug" style="background:linear-gradient(135deg,#cfc9c2,#6e6158)"></div><div class="badge"></div><h4>Lorem ipsum dolor</h4><p>consectetur adipiscing elit, sed do eiusmod tempor</p><span class="more">View All</span></article>
    <article class="card" style="left:753px"><div class="pic" role="img" aria-label="Therapist comforting a client"></div><div class="badge"></div><h4>Lorem ipsum dolor</h4><p>consectetur adipiscing elit, sed do eiusmod tempor</p><span class="more">View All</span></article>
    <a class="btn" style="left:430px;top:1510px;width:143px;height:28px;font-size:13px">View All</a>
  </section>

  <!-- why choose us -->
  <section>
    <p class="center abs" style="left:0;top:1642px;width:1010px;color:var(--orange);font-size:12px">Why choose Us</p>
    <h2 class="h2 center abs" style="left:0;top:1662px;width:1010px;font-size:31px;line-height:37px">Mental wellness<br>starts here</h2>
    <div class="abs" style="left:350px;top:1755px;width:295px;height:295px;border-radius:50%;background:radial-gradient(#fff 60%,#efefef);box-shadow:0 0 30px rgba(0,0,0,.08)"></div>
    <div class="photo" role="img" aria-label="Head silhouette filled with a tree in a sunset meadow" style="left:380px;top:1760px;width:230px;height:290px;border-radius:48% 52% 20% 40%;background:linear-gradient(180deg,#e9b56a,#9c8a3c 55%,#5f6b24)"></div>
    <div class="value" style="left:122px;top:1780px"><h5><i></i>Value one</h5><p>Lorem ipsum dolor sit amet, consectetur adipiscing elit, sed do eiusmod tempor incididunt ut labore</p></div>
    <div class="value" style="left:122px;top:1900px"><h5><i></i>Value one</h5><p>Lorem ipsum dolor sit amet, consectetur adipiscing elit, sed do eiusmod tempor incididunt ut labore</p></div>
    <div class="value" style="left:122px;top:2000px"><h5><i></i>Value one</h5><p>Lorem ipsum dolor sit amet, consectetur adipiscing elit, sed do eiusmod tempor incididunt ut labore</p></div>
    <div class="value" style="left:710px;top:1780px"><h5><i></i>Value one</h5><p>Lorem ipsum dolor sit amet, consectetur adipiscing elit, sed do eiusmod tempor incididunt ut labore</p></div>
    <div class="value" style="left:710px;top:1900px"><h5><i></i>Value one</h5><p>Lorem ipsum dolor sit amet, consectetur adipiscing elit, sed do eiusmod tempor incididunt ut labore</p></div>
    <div class="value" style="left:710px;top:2000px"><h5><i></i>Value one</h5><p>Lorem ipsum dolor sit amet, consectetur adipiscing elit, sed do eiusmod tempor incididunt ut labore</p></div>
    <p class="copy center abs" style="left:280px;top:2075px;width:450px">Lorem ipsum dolor sit amet, consectetur adipiscing elit, sed do eiusmod tempor incididunt ut labore et dolore magna aliqua. Quis ipsum suspendisse</p>
    <a class="btn" style="left:453px;top:2127px;width:107px;height:29px;font-size:12px">Contact us</a>
  </section>

  <!-- team -->
  <section>
    <div class="abs" style="left:0;top:2242px;width:274px;height:60px;background:var(--orange);border-radius:0 0 40px 0"></div>
    <h2 class="h2 abs" style="left:117px;top:2252px;font-size:33px">A Team</h2>
    <h2 class="h2 abs" style="left:117px;top:2310px;font-size:33px;line-height:43px">That Listens,<br>Understands,<br>and Supports</h2>
    <p class="abs" style="left:117px;top:2455px;width:300px;font-size:9px;line-height:11px;color:#444">At Velora Health, we provide modern, science-backed mental health services with a human touch. Located in the heart of Washington, DC, our licensed therapists</p>
    <div class="abs" style="left:704px;top:2452px;width:306px;height:150px;background:var(--orange);border-bottom-left-radius:120px"></div>
    <div class="arch" style="left:475px"><div role="img" aria-label="Smiling doctor with stethoscope" style="background:linear-gradient(180deg,#eef3f4,#c8d7da)"></div></div>
    <div class="arch" style="left:621px"><div role="img" aria-label="Smiling woman in a blazer" style="background:linear-gradient(180deg,#eef3f4,#bdb3a8)"></div></div>
    <div class="arch" style="left:762px"><div role="img" aria-label="Smiling man in a navy sweater" style="background:linear-gradient(180deg,#eef3f4,#2e3a55)"></div></div>
    <p class="abs" style="left:474px;top:2512px;color:var(--orange);font-size:15px;font-weight:600">Meet Our Therapists</p>
  </section>

  <!-- testimonials -->
  <section>
    <h2 class="h2 center abs" style="left:0;top:2650px;width:1010px">What Our Clients Say</h2>
    <div class="review" style="left:122px;top:2808px;width:228px;height:127px"><div class="who"><i></i><span>Owen Haskell<br>Location: Madrid, Spain</span></div><p>At Velora Health, they provide modern, health services with a human touch.</p><div class="stars">★★★★★</div></div>
    <div class="review sm" style="left:374px;top:2737px;width:256px;height:133px"><div class="who"><i></i><span>Mateo Linares<br>Location: Madrid, Spain</span></div><p>At Velora Health, they provide modern, science-backed mental health services with a human touch. Located in the heart of Washington, DC, our licensed therapists. At Velora Health, they provide modern care with warmth and a human touch in DC.</p><div class="stars">★★★★★</div></div>
    <div class="review sm" style="left:374px;top:2890px;width:256px;height:130px"><div class="who"><i></i><span>Mateo Linares<br>Location: Madrid, Spain</span></div><p>At Velora Health, they provide modern, science-backed mental health services with a human touch. Located in the heart of Washington, DC, our licensed therapists. At Velora Health, they provide modern care with warmth and a human touch in DC.</p><div class="stars">★★★★★</div></div>
    <div class="review" style="left:653px;top:2812px;width:228px;height:128px"><div class="who"><i></i><span>Anika Desai<br>Location: Pune</span></div><p>At Velora Health, they provide modern, health services with a human touch.</p><div class="stars">★★★★★</div></div>
  </section>

  <!-- contact form -->
  <section class="form">
    <h2 class="h2 abs" style="left:106px;top:3176px;font-size:31px;line-height:37px">Ready to Begin<br>Your Healing Journey?</h2>
    <label style="left:109px;top:3272px">Name</label><div class="field" style="top:3270px;height:26px"></div>
    <label style="left:109px;top:3310px">Email</label><div class="field" style="top:3308px;height:26px"></div>
    <label style="left:107px;top:3347px">Content</label><div class="field" style="top:3345px;height:66px"></div>
    <a class="btn" style="left:304px;top:3428px;width:115px;height:25px;font-size:15px">Send</a>
    <svg class="abs" style="left:0;top:3460px" width="200" height="95"><path d="M0 0 L60 0 A135 95 0 0 1 195 95 L0 95Z" fill="var(--orange-deep)"/></svg>
    <div class="abs" style="left:538px;top:3150px;width:240px;height:340px;border-left:2px solid var(--orange);border-top:2px solid var(--orange)"></div>
    <div class="photo" role="img" aria-label="Confident young man pointing forward with colleagues" style="left:554px;top:3165px;width:214px;height:315px;background:linear-gradient(180deg,#dedad5,#8b6a4c 60%,#3a3a3a)"></div>
    <div class="abs" style="left:790px;top:3480px;width:100px;height:2px;background:var(--orange)"></div>
    <div class="abs" style="left:890px;top:3150px;width:120px;height:60px;background:var(--orange);border-radius:60px 0 0 0"></div>
    <div class="photo" role="img" aria-label="Friends laughing together indoors" style="left:803px;top:3210px;width:207px;height:230px;background:linear-gradient(135deg,#d8d4ce,#6f6459)"></div>
    <div class="abs" style="left:890px;top:3440px;width:120px;height:95px;background:var(--orange)"></div>
  </section>

  <!-- footer -->
  <footer>
    <div class="brand abs" style="left:81px;top:3612px;font-size:44px">Velora Health</div>
    <p class="abs" style="left:81px;top:3680px;font-size:13px;line-height:17px;color:#555">Our latest news and important announcecf.<br>Our latest news and important.</p>
    <div class="social"><i></i><i></i><i></i></div>
    <nav class="footer-links"><span>About</span><span>Services</span><span>Careers</span><span>Blog</span><span>Privacy Policy</span></nav>
    <div class="abs" style="left:623px;top:3743px;display:flex;align-items:center;gap:10px;font-size:11px;color:#444">
      <svg width="20" height="20" viewBox="0 0 20 20"><circle cx="10" cy="10" r="10" fill="var(--orange)"/><path d="M6.5 5.5l2 0 1 2.5-1.3 1a6 6 0 0 0 2.8 2.8l1-1.3 2.5 1v2a1.3 1.3 0 0 1-1.4 1.2A8.5 8.5 0 0 1 5.3 6.9 1.3 1.3 0 0 1 6.5 5.5z" fill="#fff"/></svg>
      (202) 555-0178</div>
    <div class="abs" style="left:792px;top:3740px;display:flex;align-items:center;gap:8px;font-size:11px;color:#444">
      <svg width="20" height="20" viewBox="0 0 20 20"><circle cx="10" cy="10" r="10" fill="var(--orange)"/><rect x="5" y="6.5" width="10" height="7" fill="none" stroke="#fff" stroke-width="1.3"/><path d="M5 7l5 4 5-4" fill="none" stroke="#fff" stroke-width="1.3"/></svg>
      hello@velorahealthdc.com</div>
    <div class="copyright">© 2025 Velora Health. All Rights Reserved.</div>
  </footer>

</main>
</body>
</html>
```